Training Consultant for Oil and Gas Drillers needs logo for business cards

I teach oil and gas professionals the skills required to keep rigs from blowing up. The company name is "Night Shift Bore Safety", which is pronounced Nite Shiffed. Tour refers to the time on an oil rig when a worker is off for sleep and rest. I teach something called Well Control, which is how to maintain a pressure balance in the well so the hydro carbons don't come to surface unexpectedly( like the Grey Tide Platform).

Target Market(s)

Rig hands and oil companies

Contact Information for Business Card

Night Shift BS ( company name) with a new logo
My name (Derek Holloway )and Title (Well Control Consultant)
Phone number and address

Font styles to use
Serif
Sans Serif

Colors

Designer to choose colors to be used in the design.

Requirements
Must have
• I need a logo for the company. I do not have anything yet

```html
<!DOCTYPE html>
<html lang="en">
<head>
<meta charset="utf-8">
<title>Night Shift BS – Business Card</title>
<link href="https://fonts.googleapis.com/css2?family=Lato:wght@400;700;900&display=swap" rel="stylesheet">
<style>
  :root {
    --stage: #3a3a3c;
    --blue-light: #0a93cf;
    --blue-deep: #0b4fa3;
    --orange: #f39118;
    --orange-light: #f6b52b;
    --ink: #333436;
    --paper: #ffffff;
  }
  * { margin: 0; padding: 0; box-sizing: border-box; }
  html, body {
    width: 1200px; height: 782px; overflow: hidden;
    background: var(--stage);
    font-family: "Lato", Arial, sans-serif;
  }
  .stage {
    width: 1200px; height: 782px;
    display: flex; align-items: center; justify-content: center; gap: 40px;
  }
  .card {
    position: relative;
    width: 540px; height: 309px;
    overflow: hidden;
    box-shadow: 0 10px 24px rgba(0,0,0,.45);
  }
  /* Front: contact side */
  .card--front { background: var(--paper); }
  .card--front .wave { position: absolute; inset: 0; width: 100%; height: 100%; }
  .brand {
    position: absolute; display: flex; align-items: center; gap: 12px;
    font-weight: 900; letter-spacing: 1px; white-space: nowrap;
  }
  .card--front .brand { left: 40px; top: 74px; font-size: 27px; color: var(--ink); }
  .brand__dot { width: 30px; height: 30px; border-radius: 50%; background: var(--orange); flex: none; }
  .contact {
    position: absolute; right: 34px; bottom: 28px;
    text-align: right; color: var(--paper);
    font-size: 15px; line-height: 1.32;
  }
  .contact__name {
    color: var(--orange); font-weight: 900; font-size: 19px;
    text-transform: uppercase; letter-spacing: .5px; line-height: 1.1;
  }
  .contact__title { margin-bottom: 6px; }
  .contact__line { display: flex; justify-content: flex-end; align-items: center; gap: 7px; }
  .contact__line svg { width: 13px; height: 13px; fill: var(--orange); flex: none; }
  .contact__line--plain { padding-right: 20px; }
  /* Back: brand side */
  .card--back {
    background: linear-gradient(200deg, var(--blue-light) 0%, var(--blue-deep) 100%);
    display: flex; align-items: center; justify-content: center;
  }
  .card--back .brand { position: static; font-size: 28px; color: var(--paper); }
  .card--back .brand__dot { background: var(--paper); }
</style>
</head>
<body>
<main class="stage">
  <section class="card card--front" aria-label="Business card front">
    <svg class="wave" viewBox="0 0 540 309" preserveAspectRatio="none" aria-hidden="true">
      <defs>
        <linearGradient id="bandGradient" x1="1" y1="0" x2="0" y2="1">
          <stop offset="0" stop-color="#0a93cf"/>
          <stop offset="1" stop-color="#0b4fa3"/>
        </linearGradient>
      </defs>
      <path d="M0 178 C120 250 230 250 320 190 C400 135 470 112 540 125 L540 309 L0 309 Z" fill="url(#bandGradient)"/>
      <path d="M0 178 C120 250 230 250 320 190 C400 135 470 112 540 125" fill="none" stroke="#f39118" stroke-width="4"/>
    </svg>
    <div class="brand"><span class="brand__dot"></span>NIGHT SHIFT BS</div>
    <div class="contact">
      <div class="contact__name">Derek Holloway</div>
      <div class="contact__title">Well Control Consultant</div>
      <div class="contact__line">041-555 020 318
        <svg viewBox="0 0 24 24"><path d="M6.6 10.8a15.1 15.1 0 0 0 6.6 6.6l2.2-2.2a1 1 0 0 1 1-.25 11.4 11.4 0 0 0 3.6.57 1 1 0 0 1 1 1V20a1 1 0 0 1-1 1A17 17 0 0 1 3 4a1 1 0 0 1 1-1h3.5a1 1 0 0 1 1 1c0 1.25.2 2.45.57 3.57a1 1 0 0 1-.25 1z"/></svg>
      </div>
      <div class="contact__line">derek@nightshiftbs.com
        <svg viewBox="0 0 24 24"><path d="M2 5h20v14H2z M2 5l10 8 10-8" stroke="#0b4fa3" stroke-width="1.5"/></svg>
      </div>
      <div class="contact__line contact__line--plain">87, Derrick Road</div>
      <div class="contact__line contact__line--plain">77410, Harrow County</div>
    </div>
  </section>

  <section class="card card--back" aria-label="Business card back">
    <div class="brand"><span class="brand__dot"></span>NIGHT SHIFT BS</div>
  </section>
</main>
</body>
</html>
```